Business Card Design Project

I have just chosen a logo and would now like this designed onto a business card for my hair salon. I would like it to be classy not to busy and have a wow factor when people look at them
Has to Include on card:
Logo Design
And business details below
Kellie-ann Drummond (owner)
0482 736 219
Rdw@vomblet.com.au
71 Willowmere Rise Corvin Cove
Logo is now attached please provide designs
Hair

```html
<!DOCTYPE html>
<html lang="en">
<head>
<meta charset="utf-8">
<title>Velour Hair Atelier – Business Card</title>
<link rel="stylesheet" href="https://fonts.googleapis.com/css2?family=Cinzel:wght@600&family=Open+Sans:wght@400&family=Roboto+Condensed:wght@400&display=swap">
<style>
  :root {
    --backdrop: #2b2b2b;
    --card-white: #f7f7f7;
    --teal: #3a9fae;
    --teal-light: #4ab0bf;
    --teal-dark: #2e8d9b;
    --magenta: #d81b78;
    --ink: #555555;
    --rule: #8a8a8a;
  }
  * { margin: 0; padding: 0; box-sizing: border-box; }
  html, body {
    width: 1200px;
    height: 900px;
    overflow: hidden;
    background: var(--backdrop);
  }
  .stage {
    position: relative;
    width: 1200px;
    height: 900px;
  }
  .card {
    position: absolute;
    left: 290px;
    width: 620px;
    height: 354px;
    overflow: hidden;
    box-shadow: 0 10px 30px rgba(0, 0, 0, 0.45);
  }

  /* Front side */
  .card--front {
    top: 80px;
    background: var(--card-white);
  }
  .front-band {
    position: absolute;
    inset: 0;
    width: 620px;
    height: 354px;
  }
  .brand {
    position: absolute;
    left: 34px;
    top: 58px;
    display: flex;
    align-items: center;
    gap: 12px;
  }
  .brand__mark {
    width: 14px;
    height: 14px;
    border-radius: 50%;
    background: var(--magenta);
  }
  .brand__name {
    font-family: "Cinzel", serif;
    font-weight: 600;
    font-size: 30px;
    line-height: 1;
    color: var(--magenta);
    letter-spacing: 0.5px;
  }
  .rule {
    position: absolute;
    height: 1px;
    background: var(--rule);
  }
  .rule--name { left: 34px; top: 134px; width: 300px; }
  .rule--contact { left: 0; top: 214px; width: 400px; }
  .holder {
    position: absolute;
    right: 70px;
    top: 112px;
    text-align: right;
    font-family: "Roboto Condensed", sans-serif;
    white-space: nowrap;
  }
  .holder__name {
    font-size: 21px;
    color: var(--teal);
    line-height: 1.1;
  }
  .holder__role {
    font-size: 13px;
    color: var(--magenta);
    margin-top: 4px;
  }
  .contact {
    position: absolute;
    left: 40px;
    top: 238px;
    list-style: none;
    font-family: "Open Sans", sans-serif;
    font-size: 14px;
    color: var(--ink);
  }
  .contact__item {
    display: flex;
    align-items: center;
    gap: 14px;
    height: 26px;
  }
  .contact__icon {
    width: 14px;
    height: 14px;
    flex: none;
  }

  /* Back side */
  .card--back {
    top: 466px;
    background: radial-gradient(ellipse at 60% 45%, var(--teal-light) 0%, var(--teal) 55%, var(--teal-dark) 100%);
    display: flex;
    align-items: center;
    justify-content: center;
  }
  .back-brand {
    font-family: "Cinzel", serif;
    font-weight: 600;
    font-size: 50px;
    color: #ffffff;
    text-align: center;
    line-height: 1.1;
    letter-spacing: 1px;
  }
</style>
</head>
<body>
<main class="stage">

  <section class="card card--front" aria-label="Business card front">
    <svg class="front-band" viewBox="0 0 620 354" aria-hidden="true">
      <polygon points="620,170 620,354 540,354" fill="var(--teal)"/>
    </svg>

    <div class="brand">
      <span class="brand__mark"></span>
      <span class="brand__name">Velour Hair Atelier</span>
    </div>

    <div class="rule rule--name"></div>

    <div class="holder">
      <p class="holder__name">Kellie-ann Drummond</p>
      <p class="holder__role">Owner</p>
    </div>

    <div class="rule rule--contact"></div>

    <ul class="contact">
      <li class="contact__item">
        <svg class="contact__icon" viewBox="0 0 24 24" aria-hidden="true">
          <path fill="var(--teal)" d="M6.6 10.8a15.1 15.1 0 0 0 6.6 6.6l2.2-2.2a1 1 0 0 1 1-.25 11.4 11.4 0 0 0 3.6.57 1 1 0 0 1 1 1V20a1 1 0 0 1-1 1A17 17 0 0 1 3 4a1 1 0 0 1 1-1h3.5a1 1 0 0 1 1 1c0 1.250.2 2.450.57 3.570a1 1 0 0 1-.25 1z"/>
        </svg>
        <span>0482 736 219</span>
      </li>
      <li class="contact__item">
        <svg class="contact__icon" viewBox="0 0 24 24" aria-hidden="true">
          <rect x="2" y="5" width="20" height="14" rx="2" fill="var(--teal)"/>
          <path d="M3 6l9 7 9-7" fill="none" stroke="#ffffff" stroke-width="1.6"/>
        </svg>
        <span>Rdw@vomblet.com.au</span>
      </li>
      <li class="contact__item">
        <svg class="contact__icon" viewBox="0 0 24 24" aria-hidden="true">
          <path fill="var(--teal)" d="M12 2a7 7 0 0 0-7 7c0 5.2 7 13 7 13s7-7.8 7-13a7 7 0 0 0-7-7zm0 9.5A2.5 2.5 0 1 1 12 6.5a2.5 2.5 0 0 1 0 5z"/>
        </svg>
        <span>71 Willowmere Rise Corvin Cove</span>
      </li>
    </ul>
  </section>

  <section class="card card--back" aria-label="Business card back">
    <p class="back-brand">Velour<br>Hair Atelier</p>
  </section>

</main>
</body>
</html>
```